Create a Design of an Insert for Hand knitting Yarn Packages

We need a new insert design for our new offering of hand knitting yarn packages (examples of such packages from competitors see photos attached).

There shall be 2 different kind of inserts:
1. 1-page insert: insert with just 1 page, which will be located only at the front of the package (about 15 cm x 20 cm)
2. Book-like insert: insert which will be folded like a book (front, side, back) around the package (about 20 cm x 30 cm)

The below information that must be on the insert (and will be exchanged according to the different articles in future). Please find an example – see file.
For the book-like insert, please find below also where each piece of information should be located.
1. Brand name (front / side / back):
“Tovalin” alternatively “Brusoka” (please see logo designs attached as file)
2. Name of the yarn, for example (front / side / back):
“Mützengarn Greta” : (=Hat Yarn Greta)
3. Short Description, for example (front / side / back):
“Kombiset für Rundschal” (=Combination Package for Scarf)
4. Space for small pictures of the available shades (front)
5. Space for a larger picture of the model with the knitting (front)
6. Composition for example (back):
“70% Polyacryl, acrylic 7 acrylique
30% Schurwolle / virgin wool / laine vierge”)

7. Small Description like this (back):
“ - 3 Knäuel ausreichend für Mütze und Schal
- schnell gehäkelt auf für Ungeübte
- Wärmend und isolierend durch Wollanteil“
8. Wording about the weight and running length (back):
“ e 100g (2 x 50g)
ca. 165m Lauflänge
mit 1 Paar Stricknadeln Nr. 4-5”
9. .Company and address (back):
“Tovalin GmbH
80637 München”
10. Barcode according Standard SC2 + Scangrade 3B (back)
11. Vernaquil Label (back) – see file
12. Care Instructions (back) – see file

We need the following designs:
1. Book design
1.1 with brand name Tovalin
1.2. with brand name Brusoka
2. 1-page design
2.1 with brand name Tovalin
2.2. with brand name Brusoka

The insert design should be simple and straightforward, but it should also give a valuable impression.

German Description
Wir benötigen ein neues Einlegerdesign für unser Angebot von Handarbeitspackungen (Beispiele solcher Packungen siehe Dateien)

Die Einleger haben grundsätzlich zwei verschiedene Größen:
1. 1-seitiger Einleger: einfacher Einleger mit nur einer Seite, die in der Vorderseite der Packung liegt (ca. 15 cm x 20 cm)
2. Einleger in Buchform: der Einleger wird gefaltet wie ein Buch (mit Vorderseite, Buchrücken, Rückseite) um die Packung herum (ca. 20 cm x 30 cm)

7. “70% Polyacryl, acrylic 7 acrylique

8. Small Description like this (back):
9. Wording about the weight and running length (back):
“ e 100g (2 x 50g)
ca. 165m Lauflänge
10. .Company and address (back):
“Tovalin GmbH
80637 München”
11. Barcode according Standard SC2 + Scangrade 3B (back)
12. Vernaquil Label (back) – see file
13. Care Instructions (back) – see file

3. Book design
4. 1-page design

Das Design sollte einfach und schlicht sein, dabei aber einen wertigen Eindruck machen.

Target Market(s)

end consumers with interest in handknitting or crocheting

Industry/Entity Type

Yarn

Font styles to use
Other font styles liked:
• should fit the overall design

Colors

Designer to choose colors to be used in the design.

Requirements
Must have
• The layout must have the possibility to include a picture of a model wearing a knitting ( for which on the back of the insert we will provide the instructions )
Nice to have
• see the samples attached - but we would like to have a more attractive design
Should not have
• The project should not be cheap looking.

```html
<!DOCTYPE html>
<html lang="de">
<head>
<meta charset="utf-8">
<title>Mützengarn Greta – Einleger</title>
<link rel="stylesheet" href="https://fonts.googleapis.com/css2?family=Alegreya:ital@1&family=Lancelot&family=Roboto+Condensed:wght@300;400&display=swap">
<style>
  :root {
    --band: #a87b47;
    --band-dark: #8f6638;
    --paper: #ead3b3;
    --paper-light: #f0dcc0;
    --ink: #1d1712;
    --frame: #8a6239;
    --cream: #f6ead8;
    --white: #ffffff;
  }
  html, body { margin: 0; padding: 0; overflow: hidden; }
  body { width: 800px; height: 1200px; background: var(--paper); }
  .insert {
    position: relative; width: 800px; height: 1200px; overflow: hidden;
    background: radial-gradient(ellipse at 50% 50%, var(--paper-light), var(--paper) 70%);
    color: var(--ink);
    font-family: "Roboto Condensed", "Arial Narrow", sans-serif;
  }
  .band-top {
    position: absolute; left: 0; top: 0; width: 800px; height: 203px;
    background: radial-gradient(ellipse at 45% 40%, #c09464, var(--band) 60%, var(--band-dark));
  }
  .band-bottom {
    position: absolute; left: 0; top: 1156px; width: 800px; height: 44px;
    background: linear-gradient(90deg, var(--band-dark), var(--band), var(--band-dark));
  }
  .brand { position: absolute; display: flex; align-items: center; gap: 10px; transform: translate(-50%, -50%); }
  .brand-dot { width: 26px; height: 26px; border: 2px solid var(--ink); border-radius: 50%; }
  .brand-name { font-family: "Lancelot", serif; font-size: 38px; letter-spacing: 3px; color: var(--ink); }
  .pack-weight {
    position: absolute; left: 636px; top: 140px;
    font-size: 34px; font-weight: 300; color: var(--cream);
  }
  .pack-weight .estimate { font-family: "Lancelot", serif; font-size: 48px; vertical-align: -4px; margin-left: 4px; }
  .yarn-name { position: absolute; margin: 0; font-family: "Lancelot", serif; font-weight: 400; font-size: 44px; line-height: 1; white-space: nowrap; }
  .yarn-set { position: absolute; margin: 0; font-size: 28px; font-weight: 400; white-space: nowrap; }
  .photo-slot {
    position: absolute; box-sizing: border-box;
    border: 2px dashed var(--frame);
    display: flex; align-items: center; justify-content: center;
    font-size: 26px; font-weight: 400;
  }
  .features { position: absolute; left: 70px; top: 888px; margin: 0; padding: 0; list-style: none;
    font-family: "Alegreya", serif; font-style: italic; font-size: 17px; line-height: 25.5px; }
  .facts { position: absolute; left: 501px; top: 942px; margin: 0; padding: 0; list-style: none;
    font-size: 14px; line-height: 23.5px; }
  .needle-info { position: absolute; left: 46px; top: 1028px; width: 48px; text-align: center; font-size: 12px; }
  .gauge { position: absolute; left: 98px; top: 1016px; }
  .care { position: absolute; left: 42px; top: 1110px; }
  .recycling { position: absolute; left: 612px; top: 1082px; }
  .company { position: absolute; left: 247px; top: 1106px; font-size: 15px; font-weight: 300; letter-spacing: 1px; line-height: 17px; }
  .code-field { position: absolute; left: 552px; top: 1111px; width: 218px; height: 89px; background: var(--white); }
</style>
</head>
<body>
<main class="insert">
  <div class="band-top"></div>

  <div class="brand" style="left:398px;top:108px"><span class="brand-dot"></span><span class="brand-name">Brusoka</span></div>
  <div class="pack-weight">2 x 50 g<span class="estimate">e</span></div>

  <!-- front -->
  <h1 class="yarn-name" style="left:47px;top:228px">Mützengarn Greta</h1>
  <p class="yarn-set" style="left:61px;top:286px">Kombiset für Rundschal</p>
  <div class="photo-slot" style="left:74px;top:337px;width:245px;height:125px" role="img" aria-label="Platz für Bilder der Farbtöne">Place picture here</div>
  <div class="photo-slot" style="left:436px;top:216px;width:334px;height:248px" role="img" aria-label="Platz für Foto des Modells mit Strickstück">Place picture here</div>

  <!-- side -->
  <div class="brand" style="left:199px;top:601px"><span class="brand-dot"></span><span class="brand-name">Brusoka</span></div>
  <h2 class="yarn-name" style="left:446px;top:542px">Mützengarn Greta</h2>
  <p class="yarn-set" style="left:471px;top:597px">Kombiset für Rundschal</p>

  <!-- back -->
  <h2 class="yarn-name" style="left:48px;top:777px">Mützengarn Greta</h2>
  <p class="yarn-set" style="left:71px;top:838px">Kombiset für Rundschal</p>
  <ul class="features">
    <li>Knäuel ausreichend für Mütze und Schal</li>
    <li>schnell gehäkelt auf für Ungeübte</li>
    <li>Wärmend und isolierend durch Wollanteil</li>
  </ul>

  <div class="brand" style="left:597px;top:825px"><span class="brand-dot"></span><span class="brand-name">Brusoka</span></div>
  <ul class="facts">
    <li>70% Polyacryl, acrylic 7 acrylique</li>
    <li>30% Schurwolle / virgin wool / laine vierge</li>
    <li>e 100g (2 x 50g)</li>
    <li>ca. 165m Lauflänge</li>
    <li>mit 1 Paar Stricknadeln Nr. 4-5</li>
  </ul>

  <div class="needle-info">
    <svg width="40" height="38" viewBox="0 0 40 38" aria-hidden="true">
      <line x1="6" y1="2" x2="6" y2="36" stroke="#1d1712" stroke-width="2"/>
      <line x1="14" y1="2" x2="34" y2="36" stroke="#1d1712" stroke-width="2"/>
      <line x1="34" y1="2" x2="14" y2="36" stroke="#1d1712" stroke-width="2"/>
    </svg>
    <div>Nr. 4-5</div>
  </div>

  <svg class="gauge" width="90" height="86" viewBox="0 0 90 86" aria-label="Maschenprobe 10 x 10 cm">
    <text x="48" y="12" font-size="9" font-family="Roboto Condensed, sans-serif" fill="#1d1712">10 x 10 cm</text>
    <rect x="21" y="18" width="50" height="51" fill="none" stroke="#1d1712" stroke-width="1"/>
    <g fill="none" stroke="#1d1712" stroke-width="0.8">
      <path d="M21 26 q6 -3 12 0 t12 0 t12 0 t14 0"/>
      <path d="M21 33 q6 -3 12 0 t12 0 t12 0 t14 0"/>
      <path d="M21 40 q6 -3 12 0 t12 0 t12 0 t14 0"/>
      <path d="M21 47 q6 -3 12 0 t12 0 t12 0 t14 0"/>
      <path d="M21 54 q6 -3 12 0 t12 0 t12 0 t14 0"/>
      <path d="M21 61 q6 -3 12 0 t12 0 t12 0 t14 0"/>
    </g>
    <text x="2" y="40" font-size="8" font-family="Roboto Condensed, sans-serif" fill="#1d1712">- - R</text>
    <text x="34" y="81" font-size="8" font-family="Roboto Condensed, sans-serif" fill="#1d1712">- - M</text>
  </svg>

  <svg class="care" width="150" height="28" viewBox="0 0 150 28" aria-label="Pflegehinweise">
    <g fill="none" stroke="#1d1712" stroke-width="1.6">
      <path d="M2 6 L6 22 H22 L26 6"/><path d="M3 8 q4 -3 8 0 t8 0 t7 0"/>
      <path d="M34 22 L44 6 L54 22 Z"/><line x1="34" y1="6" x2="54" y2="24"/><line x1="54" y1="6" x2="34" y2="24"/>
      <rect x="62" y="7" width="20" height="16"/><circle cx="72" cy="15" r="6"/><line x1="60" y1="5" x2="84" y2="25"/><line x1="84" y1="5" x2="60" y2="25"/>
      <path d="M92 20 H112 L110 12 H98 Q93 12 92 20 Z"/><line x1="90" y1="6" x2="114" y2="24"/><line x1="114" y1="6" x2="90" y2="24"/>
      <circle cx="132" cy="14" r="10"/><line x1="122" y1="26" x2="142" y2="26"/>
    </g>
    <text x="6.5" y="19" font-size="8" font-family="Roboto Condensed, sans-serif" fill="#1d1712">30</text>
    <text x="128" y="18.5" font-size="12" font-family="Roboto Condensed, sans-serif" fill="#1d1712">P</text>
  </svg>

  <svg class="recycling" width="110" height="34" viewBox="0 0 110 34" aria-label="Recyclinghinweise">
    <circle cx="12" cy="12" r="10" fill="#1d1712"/>
    <path d="M7 12 a5 5 0 1 1 5 5" fill="none" stroke="#ead3b3" stroke-width="2"/>
    <g fill="none" stroke="#1d1712" stroke-width="1.6">
      <path d="M34 20 L44 3 L54 20 Z"/>
      <path d="M62 20 L72 3 L82 20 Z"/>
    </g>
    <text x="35" y="31" font-size="7" font-family="Roboto Condensed, sans-serif" fill="#1d1712">PAP</text>
    <text x="67" y="31" font-size="7" font-family="Roboto Condensed, sans-serif" fill="#1d1712">PE</text>
    <circle cx="98" cy="4" r="3" fill="#1d1712"/>
    <rect x="93" y="9" width="12" height="13" fill="#1d1712"/>
  </svg>

  <address class="company" style="font-style:normal">Tovalin&nbsp; GmbH<br>80637&nbsp; München</address>

  <div class="band-bottom"></div>
  <div class="code-field"></div>
</main>
</body>
</html>
```